Construction Company Website Design

I need a Website Design for a Construction Company. I have attached logo and business card design files (a.i) to match styles and text for the website. I will need design for 3 pages:
1. A Home page
2. A secondary page (will be different information pages)
3. A contact page with submision form
Website to look professional and match the 'theme' across all pages, using main colours / reverse colours as per design files. Must be clear it is a construction related website without being over the top. Happy for the construction related details (whether that be images/outlines/backgrounds etc to be fairly subtle and not overbearing on the contect of the pages. It will be the content that will be most important, not the images within.

Content has not yet been fully completed but attached is a site map. Each page will need a space for the insertion of the relevant heading and associated content for that particular page. Example can be used as per attached map. If it is preferable to have content completed for this to be a more succesful project please advise and I will complete and submit.

Target Market(s)

Clients for potential construction projects. These could be a range of people. All would be very professional, well educated and put a substantial expection on the quality of website provided.

Industry/Entity Type

Construction

Number of Pages Required

3 page

Font styles to use
Serif
Sans Serif
Other font styles liked:
• fonts preferable as per design files provided unless designer beleives a different font would suit better

Requirements
Must have
• Colour scheme to match logo and business card files provided. Fonts that match as per provided files. Pages must be consistent with the theme carrying across all pages. All pages must have contact details at the bottom of the page.
• Contents of page 1 - 'Home page': multiple tab options / logo link
• Contents of page 2 - 'Secondary page': Top and side navigation / area for information and/or images.
• Contents of page - 'Contact us page': Top and side navigation / Submission form / area for logos such as linkdin, facebook etc.
Nice to have
• Would be good to have a or some generic construction related images - outlines / shadows / effects etc. These might be background images or outlines related to the relevant industry and are consistent across the pages. Could be outlines of buildings, images of men with hardhats etc etc. Good to see colour scheme as per design files used
Should not have
• No pictures of houses. Generally no photos. If any imagery of people must not show faces/details.

```html
<!DOCTYPE html>
<html lang="en">
<head>
<meta charset="utf-8">
<title>Ridgeline Constructions</title>
<link href="https://fonts.googleapis.com/css2?family=Open+Sans:wght@400;600;700&display=swap" rel="stylesheet">
<style>
:root{
  --blue:#1aa3e8;
  --blue-dark:#0d86c4;
  --ink:#222;
  --text:#666;
  --dark:#1d1d1d;
  --darker:#141414;
  --line:#e4e4e4;
  --white:#fff;
}
*{box-sizing:border-box;margin:0;padding:0}
html,body{width:1200px;height:3100px;overflow:hidden}
body{font-family:"Open Sans",Arial,sans-serif;color:var(--ink);background:var(--white);font-size:13px}
.btn{display:inline-block;background:var(--blue);color:#fff;font-size:11px;font-weight:600;padding:9px 20px;border-radius:2px}
.btn-dark{background:#333}
.section-title{text-align:center;font-size:19px;font-weight:700}
.section-title::after{content:"";display:block;width:36px;height:3px;background:var(--blue);margin:12px auto 0}

/* hero + header */
.hero{position:relative;height:450px;background:linear-gradient(90deg,#2b2b2b,#4a4a4a 55%,#3a3a3a)}
.topbar{height:20px;background:#151515;display:flex;align-items:center;justify-content:space-between;padding:0 150px;font-size:9px;color:#bbb}
.topbar .contacts{display:flex;gap:26px}
.topbar .contacts span::before{content:"";display:inline-block;width:6px;height:6px;border-radius:50%;background:var(--blue);margin-right:6px}
.navbar{position:relative;z-index:3;height:90px;display:flex;align-items:center;justify-content:space-between;padding:0 150px;border-bottom:1px solid rgba(255,255,255,.12)}
.brand{display:flex;align-items:center;gap:10px;color:#fff;font-size:18px;font-weight:600;letter-spacing:2px}
.brand .mark{width:14px;height:14px;background:var(--blue)}
.menu{display:flex;align-items:center;gap:24px;font-size:11px;color:#ddd;position:relative}
.menu .active{color:var(--blue)}
.menu .btn{padding:7px 16px;background:transparent;border:1px solid var(--blue);color:#fff}
.dropdown{position:absolute;z-index:4;top:30px;left:52px;width:120px;background:#222;padding:8px 0;font-size:9px;color:#ccc;white-space:nowrap}
.dropdown div{padding:6px 12px}
.dropdown div:first-child{color:var(--blue)}
.hero-copy{position:absolute;left:150px;top:180px;width:340px;color:#ddd}
.hero-copy h1{color:var(--blue);font-size:20px;font-weight:700;margin-bottom:12px}
.hero-copy p{font-size:10px;line-height:1.7;margin-bottom:20px}
.hero-art{position:absolute;z-index:1;left:740px;top:120px;width:250px;height:250px;border-radius:50%;background:radial-gradient(circle,#35b4f0,var(--blue) 65%)}

/* services */
.services{height:450px;padding-top:50px;text-align:center}
.service-row{display:flex;justify-content:center;gap:120px;margin:60px 0 44px}
.service{width:180px}
.service .icon{width:80px;height:80px;border:2px solid var(--blue);border-radius:50%;margin:0 auto 18px;display:flex;align-items:center;justify-content:center}
.service h3{font-size:13px;font-weight:700;margin-bottom:8px}
.service h3::after{content:"";display:block;width:24px;height:2px;background:var(--blue);margin:8px auto 0}
.service p{font-size:10px;line-height:1.6;color:var(--text)}

/* projects */
.projects-head{height:175px;padding-top:50px;background:linear-gradient(180deg,#f2f8fc,#eaf3f9)}
.filters{display:flex;justify-content:center;gap:34px;margin-top:32px;font-size:9px;color:#888}
.filters .on{color:var(--ink);font-weight:700}
.grid{display:grid;grid-template-columns:repeat(3,400px);grid-template-rows:repeat(2,283px)}
.tile{position:relative}
.tile.roof{background:linear-gradient(135deg,#b5552b,#8c3c1f)}
.tile.paint{background:linear-gradient(135deg,#5fb6d8,#2e8fb8)}
.tile.tiles{background:linear-gradient(135deg,#cfcac2,#8f8a84)}
.tile.house{background:linear-gradient(180deg,#8fb5d6,#e7dcc7 55%,#c9b69a)}
.tile.barn{background:linear-gradient(180deg,#b8cbd8,#3b3b3b 60%,#5a5a5a)}
.tile.room{background:linear-gradient(180deg,#3d3d3d,#1f1f1f)}
.overlay{position:absolute;inset:0;background:rgba(26,163,232,.82);display:flex;flex-direction:column;align-items:center;justify-content:center;color:#fff;font-size:11px;gap:10px}
.projects-foot{height:120px;display:flex;align-items:center;justify-content:center}

/* news */
.news{height:440px;padding-top:10px}
.cards{display:flex;justify-content:center;gap:20px;margin-top:40px}
.card{width:226px}
.card .photo{height:115px;background:linear-gradient(135deg,#d8c3a8,#9c8266)}
.card:nth-child(2) .photo{background:linear-gradient(135deg,#e8c26a,#b48a3c)}
.card:nth-child(3) .photo{background:linear-gradient(135deg,#b9c6cf,#6f7f8c)}
.card h4{display:flex;gap:8px;font-size:10px;font-weight:700;line-height:1.4;margin:12px 0 8px}
.card h4 span{flex:none;width:22px;height:22px;background:var(--blue)}
.card p{font-size:9px;line-height:1.6;color:var(--text);margin-bottom:14px}

/* cta */
.cta{height:115px;background:var(--blue);display:flex;align-items:center;justify-content:center;gap:30px;color:#fff;font-size:16px;font-weight:700}

/* contact */
.contact{height:685px;background:linear-gradient(180deg,#262626,#1b1b1b);color:#fff;padding-top:55px}
.contact .section-title{color:#fff}
.form{width:600px;margin:40px auto 0;display:grid;grid-template-columns:1fr 1fr;gap:12px}
.field{height:28px;border:1px solid #555;font-size:9px;color:#999;padding:8px}
.field.msg{grid-column:1/3;height:130px}
.form .btn{grid-column:1/3;justify-self:center;margin-top:30px}
.info{display:flex;justify-content:center;gap:120px;margin-top:110px;text-align:center;font-size:9px;color:#bbb}
.info .ic{width:46px;height:46px;border-radius:50%;background:var(--blue);margin:0 auto 14px;display:flex;align-items:center;justify-content:center}

/* footer */
.footer{height:120px;background:var(--darker);display:flex;align-items:center;justify-content:space-between;padding:0 150px;color:#888;font-size:9px;text-align:right;line-height:1.6}
.footer .brand{font-size:15px}
</style>
</head>
<body>

<header class="hero">
  <div class="topbar">
    <span>English ▾</span>
    <div class="contacts"><span>0-000-000-0000</span><span>hello@ridgelinebuild.com</span><span>www.ridgelinebuild.com</span></div>
  </div>
  <nav class="navbar">
    <div class="brand"><span class="mark"></span>RIDGELINE CONSTRUCTIONS</div>
    <div class="menu">
      <span>Home</span><span class="active">Services</span><span>Projects</span><span>Contact</span><span>News</span>
      <span class="btn">Contact</span>
      <div class="dropdown"><div>Renovations</div><div>Painting Services</div><div>Roofing Works</div><div>Project Management</div></div>
    </div>
  </nav>
  <div class="hero-copy">
    <h1>Welcome to Our Company!</h1>
    <p>We plan, build and finish homes and commercial spaces with care, using skilled trades and quality materials. From first sketch to final handover, our team keeps every project on time, on budget and built to last for years.</p>
    <span class="btn">Learn More</span>
  </div>
  <div class="hero-art" role="img" aria-label="Blue circle with paint brushes and colour swatches"></div>
</header>

<section class="services">
  <h2 class="section-title">Our Services</h2>
  <div class="service-row">
    <div class="service">
      <div class="icon"><svg width="34" height="34" viewBox="0 0 34 34" fill="none" stroke="#1aa3e8" stroke-width="2.5" stroke-linecap="round"><path d="M6 28 22 12"/><path d="M20 6a6 6 0 0 0 8 8"/><path d="M6 6l22 22"/><path d="M4 8l4-4"/></svg></div>
      <h3>Lorem Ipsum is Simply</h3>
      <p>Careful repairs and full renovations for homes and offices of every size.</p>
    </div>
    <div class="service">
      <div class="icon"><svg width="34" height="34" viewBox="0 0 34 34" fill="none" stroke="#1aa3e8" stroke-width="2.5"><rect x="4" y="6" width="26" height="22"/><path d="M4 13h26M4 20h26M13 6v7M21 13v7M13 20v8"/></svg></div>
      <h3>Lorem Ipsum is Simply</h3>
      <p>Solid brickwork, framing and structural builds made by trusted trades.</p>
    </div>
    <div class="service">
      <div class="icon"><svg width="34" height="34" viewBox="0 0 34 34" fill="none" stroke="#1aa3e8" stroke-width="2.5"><rect x="7" y="4" width="20" height="26"/><path d="M11 11h12M11 17h12M11 23h7"/></svg></div>
      <h3>Lorem Ipsum is Simply</h3>
      <p>Clear plans, permits and project management from start to handover.</p>
    </div>
  </div>
  <span class="btn">Read More</span>
</section>

<section class="projects">
  <div class="projects-head">
    <h2 class="section-title">Recent Projects</h2>
    <div class="filters"><span class="on">All</span><span>Renovation</span><span>Painting</span><span>Roofing</span><span>Flooring</span><span>Exterior</span><span>Interior</span></div>
  </div>
  <div class="grid">
    <div class="tile roof" role="img" aria-label="Terracotta tiled roof"></div>
    <div class="tile paint" role="img" aria-label="Wall being painted blue">
      <div class="overlay"><svg width="24" height="24" viewBox="0 0 24 24" fill="none" stroke="#fff" stroke-width="2"><circle cx="10" cy="10" r="7"/><path d="M15 15l6 6"/></svg>Lorem Ipsum is Simply dummy</div>
    </div>
    <div class="tile tiles" role="img" aria-label="Floor tiles being laid"></div>
    <div class="tile house" role="img" aria-label="Rendered building with tiled roof"></div>
    <div class="tile barn" role="img" aria-label="Dark timber building under sky"></div>
    <div class="tile room" role="img" aria-label="Empty interior room"></div>
  </div>
  <div class="projects-foot"><span class="btn">All Projects</span></div>
</section>

<section class="news">
  <h2 class="section-title">News</h2>
  <div class="cards">
    <article class="card">
      <div class="photo" role="img" aria-label="Person working at a laptop"></div>
      <h4><span></span>Lorem Ipsum is Simply dummy typesetting industry</h4>
      <p>Our latest renovation wrapped up ahead of schedule, with a fresh layout, new fittings and a bright modern finish the owners love.</p>
      <span class="btn">Continue Reading</span>
    </article>
    <article class="card">
      <div class="photo" role="img" aria-label="Person relaxing in a new home"></div>
      <h4><span></span>Lorem Ipsum is Simply dummy typesetting industry</h4>
      <p>Planning a build this year? Here are a few simple steps to set a budget, pick materials and choose the right team for the job.</p>
      <span class="btn">Continue Reading</span>
    </article>
    <article class="card">
      <div class="photo" role="img" aria-label="Family at home"></div>
      <h4><span></span>Lorem Ipsum is Simply dummy typesetting industry</h4>
      <p>We have expanded our roofing crew, so we can now take on larger projects across the region with shorter wait times for clients.</p>
      <span class="btn">Continue Reading</span>
    </article>
  </div>
</section>

<section class="cta">
  <span>Call 0-000-000-0000 to Get Your Cash Offer Today</span>
  <span class="btn btn-dark">Get a free estimate</span>
</section>

<section class="contact">
  <h2 class="section-title">Contact</h2>
  <form class="form">
    <div class="field">Name</div>
    <div class="field">Email Address</div>
    <div class="field msg">Message</div>
    <span class="btn">Submit</span>
  </form>
  <div class="info">
    <div><div class="ic"><svg width="18" height="18" viewBox="0 0 24 24" fill="#fff"><path d="M12 2a7 7 0 0 0-7 7c0 5 7 13 7 13s7-8 7-13a7 7 0 0 0-7-7zm0 10a3 3 0 1 1 0-6 3 3 0 0 1 0 6z"/></svg></div>180 Grove Street, Any Town</div>
    <div><div class="ic"><svg width="18" height="18" viewBox="0 0 24 24" fill="#fff"><path d="M6.6 10.8a15 15 0 0 0 6.6 6.6l2.2-2.2a1 1 0 0 1 1-.25 11 11 0 0 0 3.6.6 1 1 0 0 1 1 1V20a1 1 0 0 1-1 1A17 17 0 0 1 3 4a1 1 0 0 1 1-1h3.5a1 1 0 0 1 1 1 11 11 0 0 0 .6 3.6 1 1 0 0 1-.25 1z"/></svg></div>0-000-000-0000</div>
    <div><div class="ic"><svg width="18" height="18" viewBox="0 0 24 24" fill="none" stroke="#fff" stroke-width="2"><rect x="3" y="5" width="18" height="14"/><path d="M3 6l9 7 9-7"/></svg></div>hello@ridgelinebuild.com</div>
    <div><div class="ic"><svg width="18" height="18" viewBox="0 0 24 24" fill="none" stroke="#fff" stroke-width="2" stroke-linecap="round"><path d="M10 14a4 4 0 0 0 6 0l3-3a4 4 0 0 0-6-6l-1 1"/><path d="M14 10a4 4 0 0 0-6 0l-3 3a4 4 0 0 0 6 6l1-1"/></svg></div>www.ridgelinebuild.com</div>
  </div>
</section>

<footer class="footer">
  <div class="brand"><span class="mark"></span>RIDGELINE CONSTRUCTIONS</div>
  <div>© 2024 Ridgeline Constructions<br>All rights reserved</div>
</footer>

</body>
</html>
```